Social Media Infographic for White Paper

Am working on a white paper on social media use by C-Suite Executives, and hope to include some infographics. I would like some help designing the first infographic.

The master bit of information is that "66% of C-Suite Executives use social media for professional purpose."

Within that 66%
-70% post original content on a daily/weekly basis
-13% of professional users are lurkers
-40% plan to use social media even more in the future

After initial design will need to two versions of the infographic, one listing the source at the bottom in small print (Source: 2017 Thornwick Partners Executive Social Media Study), the other one with no source information.

Infographic design should be complimentary with my website: www.thornwickpartners.example, but use of green should be very limited, if at all.

Target Market(s)

New media, C-Suite Executives, Executive Coaches

Industry/Entity Type

Management Consulting

Font styles to use
Sans Serif

Requirements
Must have
• Infographic with data displayed in a easy to understand format that tells the story of C-Suite Executives that participate in social media for professional purposes.
Nice to have
• Complements website design - www.thornwick.example.
Should not have
• Limit use of green from website logo, which can be overpowering. Some is ok, but not too much

```html
<!DOCTYPE html>
<html lang="en">
<head>
<meta charset="utf-8">
<title>C-Suite Executives on Social Media – Infographic</title>
<link rel="stylesheet" href="https://fonts.googleapis.com/css2?family=Roboto+Condensed:wght@700&family=Raleway:wght@400;500;800;900&family=Montserrat:wght@700&display=swap">
<style>
  :root {
    --page-bg: #f2f2f2;
    --band-sand: #ddd3a3;
    --band-grey: #e8e8e8;
    --accent-red: #9a3a2e;
    --ink: #1b1b1b;
    --stat-blue: #1f5a8a;
    --text-dark: #1c1c1c;
  }
  * { box-sizing: border-box; margin: 0; padding: 0; }
  html, body {
    width: 1200px; height: 1200px; overflow: hidden;
    background: var(--page-bg);
  }
  .infographic {
    position: absolute; left: 310px; top: 20px;
    width: 580px; height: 1160px;
    background: var(--band-grey);
    font-family: "Raleway", Arial, sans-serif;
    color: var(--text-dark);
    overflow: hidden;
  }
  .intro-band {
    position: absolute; left: 0; top: 0; width: 580px; height: 446px;
    background: var(--band-sand);
  }
  .abs { position: absolute; }
  .center { left: 0; width: 580px; text-align: center; }
  .kicker {
    top: 24px;
    font-family: "Roboto Condensed", Arial, sans-serif;
    font-weight: 700; font-size: 25px; color: var(--accent-red);
    letter-spacing: 0.2px;
  }
  .hero-stat {
    top: 44px;
    font-family: "Raleway", Arial, sans-serif;
    font-weight: 900; font-size: 122px; line-height: 1;
    color: var(--ink); font-variant-numeric: lining-nums;
    letter-spacing: -2px;
  }
  .hero-caption {
    top: 154px; font-size: 25px; font-weight: 500; color: var(--accent-red);
  }
  .art {
    border-radius: 18px;
  }
  .art-social {
    left: 110px; top: 186px; width: 364px; height: 253px;
    background: radial-gradient(ellipse at center, #3f86b8 0%, #a4483c 45%, rgba(221,211,163,0) 75%);
  }
  .section-title {
    top: 452px;
    font-weight: 800; font-size: 29px; color: var(--accent-red);
    letter-spacing: 0.3px;
  }
  .section-sub { top: 496px; font-size: 25px; font-weight: 500; }
  .stat-number {
    font-weight: 800; font-size: 98px; line-height: 1;
    color: var(--stat-blue); font-variant-numeric: lining-nums;
    letter-spacing: -1px;
  }
  .stat-label {
    font-size: 18px; font-weight: 500; line-height: 23px;
    text-align: center; text-transform: uppercase;
  }
  .art-megaphone {
    left: 51px; top: 554px; width: 143px; height: 120px;
    background: linear-gradient(135deg, #7fa6c4 0%, #c9c9c9 55%, #b8322c 100%);
  }
  .art-magnifier {
    left: 297px; top: 707px; width: 167px; height: 158px;
    background: radial-gradient(circle at 45% 40%, #f4f4f4 0%, #bcbcbc 45%, #2e77b6 75%, rgba(232,232,232,0) 90%);
    border-radius: 50%;
  }
  .art-team {
    left: 91px; top: 905px; width: 122px; height: 123px;
    background: radial-gradient(circle at 50% 40%, #5aa7e0 0%, #1c6cb0 60%, #8a8f96 100%);
    border-radius: 50%;
  }
  .stat-70 { left: 230px; top: 539px; }
  .label-70 { left: 185px; top: 634px; width: 300px; }
  .stat-13 { left: 82px; top: 712px; }
  .label-13 { left: 62px; top: 804px; width: 240px; }
  .stat-40 { left: 258px; top: 895px; }
  .label-40 { left: 220px; top: 991px; width: 300px; }
  .source {
    top: 1087px;
    font-family: "Montserrat", Arial, sans-serif;
    font-weight: 700; font-size: 12px; color: var(--ink);
  }
</style>
</head>
<body>
<main class="infographic">
  <section class="intro-band">
    <p class="abs center kicker">THE MASTER BIT OF INFORMATION IS THAT</p>
    <p class="abs center hero-stat">66%</p>
    <p class="abs center hero-caption">of C-Suite Executives use</p>
    <div class="abs art art-social" role="img" aria-label="Illustrated cluster of devices, chat bubbles and icons around the words Social Media"></div>
  </section>

  <h1 class="abs center section-title">FOR PROFESSIONAL PURPOSE</h1>
  <p class="abs center section-sub">Within that 66%</p>

  <div class="abs art art-megaphone" role="img" aria-label="Illustration of a megaphone with a tablet and phone showing charts"></div>
  <p class="abs stat-number stat-70">70%</p>
  <p class="abs stat-label label-70">Post original content<br>on a daily/weekly basis</p>

  <p class="abs stat-number stat-13">13%</p>
  <p class="abs stat-label label-13">Of professional<br>users are lurkers</p>
  <div class="abs art-magnifier" role="img" aria-label="Illustration of a magnifying glass over letters and a rising bar chart"></div>

  <div class="abs art-team" role="img" aria-label="Illustration of three business people in front of a globe"></div>
  <p class="abs stat-number stat-40">40%</p>
  <p class="abs stat-label label-40">Plan to use social media<br>even more in the future</p>

  <p class="abs center source">Source: 2017 Thornwick Partners Executive Social Media Study</p>
</main>
</body>
</html>
```